Logo and Business Card for Dental Office

We are opening a periodontal office (dental specialist for dental implants and gum diseases). It is a brand new state of the art facility with a focus on the most effective treatments for retaining natural teeth, or replacing teeth with implants when they must be lost. Strong emphasis on customer service and amenities for patient comfort. We are located just outside of Boston, MA.

Target Market(s)

potential adult patients, dentists in the community that will refer patients for specialized care

Industry/Entity Type

Dental

Requirements
Must have
• business name, address, phone number, website
Marcus T. Velloran, DMD LLC
274 Kestrel Lane, Ste 305
Harrow Glen, ME 04123
508-555-0172
508-555-0189 Fax
DrVelloran-example.com

the uploaded file has a rough version of what I'm looking for in the logo, I like the colors but it can be varies some.
Nice to have
• simple logo or symbol on business card, one possible idea I had was an abstract symbol of a screw or threads that might represent a dental implant, the attached file gives an idea of where to start.
Should not have
• I want a professional feel, no cartoons of teeth that appear childish, etc
The font should be easy to read with no curly/swirly shapes.

```html
<!DOCTYPE html>
<html lang="en">
<head>
<meta charset="utf-8">
<title>Periodontics &amp; Dental Implants – Business Card</title>
<link rel="stylesheet" href="https://fonts.googleapis.com/css2?family=Quicksand:wght@500;600&display=swap">
<style>
  :root {
    --stage: #2a2a2a;
    --card: #141414;
    --cyan: #5ccbd9;
    --white: #ffffff;
    --ink: #111111;
    --dash: #6a6a6a;
  }
  * { margin: 0; padding: 0; box-sizing: border-box; }
  html, body { width: 1200px; height: 723px; overflow: hidden; }
  body {
    background: var(--stage);
    font-family: "Quicksand", sans-serif;
    position: relative;
  }
  .card {
    position: absolute;
    top: 213px;
    width: 520px;
    height: 297px;
    background: var(--card);
    overflow: hidden;
  }
  .card--front { left: 50px; }
  .card--back { left: 630px; }

  .ring-texture {
    position: absolute;
    right: 0; top: 0;
    width: 55%; height: 100%;
    background: linear-gradient(120deg, rgba(255,255,255,0) 0%, rgba(255,255,255,0.025) 100%);
  }

  .brand {
    position: absolute;
    top: 44px; left: 0; right: 0;
    display: flex;
    justify-content: center;
    align-items: center;
    gap: 10px;
  }
  .brand__dot {
    width: 22px; height: 22px;
    border-radius: 50%;
    background: var(--white);
  }
  .brand__name {
    color: var(--white);
    font-weight: 500;
    font-size: 15px;
    line-height: 17px;
    letter-spacing: 0.5px;
    text-transform: uppercase;
  }

  .divider {
    position: absolute;
    top: 104px; left: 90px; right: 90px;
    border-top: 1px dashed var(--dash);
  }

  .doctor {
    position: absolute;
    top: 118px; left: 0; right: 0;
    text-align: center;
    color: var(--cyan);
    font-weight: 500;
    font-size: 24px;
    letter-spacing: 0.3px;
  }

  .address {
    position: absolute;
    top: 160px; left: 50%;
    transform: translateX(-50%);
    background: var(--white);
    color: var(--ink);
    font-weight: 600;
    font-size: 12px;
    padding: 4px 12px;
    white-space: nowrap;
  }

  .contacts {
    position: absolute;
    top: 204px; left: 0; right: 0;
    display: flex;
    justify-content: center;
    gap: 46px;
  }
  .contact, .website {
    display: flex;
    align-items: center;
    gap: 10px;
    color: var(--cyan);
    font-weight: 500;
    font-size: 12px;
  }
  .website {
    position: absolute;
    top: 240px; left: 0; right: 0;
    justify-content: center;
  }
  .icon { width: 20px; height: 20px; flex: none; }
</style>
</head>
<body>

<section class="card card--front" aria-label="Business card front">
  <div class="ring-texture" role="img" aria-label="Faint ring pattern texture"></div>

  <div class="brand">
    <span class="brand__dot"></span>
    <span class="brand__name">Periodontics &amp;<br>Dental Implants</span>
  </div>

  <div class="divider"></div>

  <h1 class="doctor">Marcus T. Velloran, DMD LLC</h1>

  <p class="address">274 Kestrel Lane, Ste 305, Harrow Glen, ME 04123</p>

  <div class="contacts">
    <p class="contact">
      <svg class="icon" viewBox="0 0 20 20" aria-hidden="true">
        <circle cx="10" cy="10" r="9" fill="none" stroke="var(--cyan)" stroke-width="1.3"/>
        <path d="M7 5.5 L8.6 5.5 L9.3 7.8 L8.3 8.7 Q9.3 10.8 11.3 11.7 L12.2 10.7 L14.5 11.4 L14.5 13 Q13.5 14.5 11.5 14 Q6.5 12.5 6 8 Q5.8 6.3 7 5.5 Z" fill="var(--cyan)"/>
      </svg>
      508-555-0172
    </p>
    <p class="contact">
      <svg class="icon" viewBox="0 0 20 20" aria-hidden="true">
        <circle cx="10" cy="10" r="9" fill="none" stroke="var(--cyan)" stroke-width="1.3"/>
        <rect x="7" y="5" width="6" height="3.5" fill="var(--cyan)"/>
        <rect x="5" y="8.5" width="10" height="4.5" rx="1" fill="var(--cyan)"/>
        <rect x="7" y="12" width="6" height="3" fill="var(--card)" stroke="var(--cyan)" stroke-width="1"/>
      </svg>
      508-555-0189
    </p>
  </div>

  <p class="website">
    <svg class="icon" viewBox="0 0 20 20" aria-hidden="true">
      <circle cx="10" cy="10" r="9" fill="none" stroke="var(--cyan)" stroke-width="1.3"/>
      <circle cx="10" cy="10" r="5" fill="none" stroke="var(--cyan)" stroke-width="1"/>
      <ellipse cx="10" cy="10" rx="2" ry="5" fill="none" stroke="var(--cyan)" stroke-width="1"/>
      <line x1="5" y1="10" x2="15" y2="10" stroke="var(--cyan)" stroke-width="1"/>
    </svg>
    DrVelloran-example.com
  </p>
</section>

<section class="card card--back" aria-label="Business card back">
  <svg width="520" height="297" viewBox="0 0 520 297" aria-hidden="true">
    <polygon points="0,0 85,0 0,150" fill="var(--cyan)"/>
    <polygon points="520,210 520,297 455,297" fill="var(--cyan)"/>
  </svg>
</section>

</body>
</html>
```